QuillaVorn needs a dashboard page designed

Redesign the dashboard shown in the provided images.

There are two images:
- dashboard.png
- dashboard-expanded.png

NOTE: The vocabulary navigation on the left will be a very long list of words 100s, so keep that in mind when you're designing both the vocab navigation and the expanded vocab popup.

In the dashboard.png picture, there needs to be a progress chart showing the word progress like the following: review 1(show it as completed) -> review 2(show the user they are here) -> review 3(unvisited) -> review 4(unvisited)

The do-not-design-this-page.png image is for your reference only. It is not to be designed. Use it to understand the overall look and feel of the website to help you create the best dashboard page possible.
Updates

Need extra days to review

Industry/Entity Type

Education English learning

Number of Pages Required

1 page

Requirements
Must have
• The main navigation and main header cannot change between pages. See the do-not-design page for the main navigateion and header.
Should not have
• Do not add a person profile. We will not have images of our users. Keep the icons in the main navigation as they are.

```html
<!DOCTYPE html>
<html lang="en">
<head>
<meta charset="utf-8">
<title>QuillaVorn Tutor – Dashboard</title>
<link href="https://fonts.googleapis.com/css2?family=Poppins:wght@400;500;600;700&display=swap" rel="stylesheet">
<style>
  :root {
    --page: #f3f3f3;
    --card: #f9f9f9;
    --rail: #3a3e43;
    --panel: #353a40;
    --ink: #2b2f33;
    --muted: #8a8f94;
    --line: #e2e2e2;
    --chip: #ececec;
    --accent-green: #7cc24a;
    --close: #ef6a5c;
    --band-long: #e4eaf1;
    --band-working: #e7efe0;
    --band-short: #f4e4e9;
    --band-forgot: #d8e6ef;
    --scrim: rgba(0, 0, 0, 0.5);
  }
  * { box-sizing: border-box; margin: 0; padding: 0; }
  html, body { width: 1200px; height: 1037px; overflow: hidden; }
  body { position: relative; background: var(--page); font-family: "Poppins", sans-serif; color: var(--ink); }
  .abs { position: absolute; }

  /* main rail */
  .main-nav { left: 17px; top: 21px; width: 77px; height: 995px; background: var(--rail); border-radius: 12px; }
  .nav-item { position: absolute; left: 0; width: 77px; text-align: center; color: #fff; font-size: 9.5px; line-height: 14px; }
  .nav-divider { position: absolute; left: 10px; width: 57px; border-top: 1px solid #50555b; }
  .home-badge { width: 35px; height: 35px; border-radius: 50%; background: #dcdcdc; margin: 0 auto 6px; display: flex; align-items: center; justify-content: center; }

  /* vocab panel */
  .vocab-panel { left: 0; top: 0; width: 297px; height: 1037px; background: var(--panel); }
  .vocab-select { left: 116px; top: 28px; width: 113px; height: 30px; border: 1px solid #6a6f75; border-radius: 3px; color: #fff; font-size: 9px; font-weight: 500; padding: 8px 12px; }
  .popout-btn { left: 282px; top: 31px; width: 25px; height: 25px; border-radius: 50%; background: #d5d5d5; }
  .panel-heading { color: #fff; font-size: 12px; font-weight: 600; }
  .panel-tag { color: var(--accent-green); font-size: 9px; font-weight: 700; }
  .panel-list { list-style: none; color: #b8bcc0; font-size: 10px; line-height: 15px; }
  .panel-list li::before { content: "›"; margin-right: 7px; }

  /* header */
  .app-title { left: 337px; top: 22px; font-size: 27px; font-weight: 700; }
  .header-rule { left: 337px; top: 102px; width: 825px; border-top: 1px solid #dcdcdc; }
  .avatar { left: 1093px; top: 33px; width: 48px; height: 48px; border-radius: 50%; background: linear-gradient(135deg, #8d8a86, #4b4846); }

  .exercise-pill { left: 820px; top: 259px; width: 342px; height: 39px; border-radius: 20px; background: #1f2226; color: #fff; font-size: 8.5px; font-weight: 700; text-align: right; padding: 14px 21px 0 0; letter-spacing: .1px; }
  .card { background: var(--card); border-radius: 15px; }
  .sentence-card { left: 337px; top: 323px; width: 824px; height: 112px; }
  .sentence-line { right: 42px; font-size: 11.5px; color: #444; white-space: nowrap; }
  .chart-card { left: 337px; top: 510px; width: 824px; height: 300px; }
  .section-title { left: 335px; top: 843px; font-size: 20px; font-weight: 600; }
  .analysis-card { left: 337px; top: 883px; width: 824px; height: 97px; padding: 18px 26px; font-size: 11.5px; line-height: 17.3px; color: #444; }

  .scrim { inset: 0; background: var(--scrim); }

  /* modal */
  .vocab-modal { left: 184px; top: 131px; width: 832px; height: 383px; background: #fff; border-radius: 30px; }
  .close-btn { left: 787px; top: 15px; width: 30px; height: 30px; border-radius: 50%; background: var(--close); }
  .modal-select { left: 43px; top: 32px; width: 285px; height: 36px; border: 1.5px solid var(--ink); border-radius: 3px; font-size: 11.5px; padding: 9px 18px; }
  .modal-rule { left: 43px; width: 746px; border-top: 1.5px solid var(--line); }
  .group-title { left: 43px; font-size: 15.5px; font-weight: 600; display: flex; align-items: center; gap: 13px; }
  .help { width: 12px; height: 12px; border: 1px solid var(--ink); border-radius: 50%; font-size: 8px; display: inline-flex; align-items: center; justify-content: center; font-weight: 500; }
  .group-tag { left: 43px; font-size: 9px; font-weight: 700; }
  .chip-row { left: 45px; display: flex; gap: 8px; }
  .chip { height: 26px; background: var(--chip); border-radius: 3px; font-size: 9.5px; display: flex; align-items: center; justify-content: center; }
</style>
</head>
<body>

<!-- underlying dashboard -->
<div class="abs vocab-panel">
  <div class="abs vocab-select">ALL <svg style="float:right;margin-top:2px" width="8" height="6" viewBox="0 0 8 6"><path d="M1 1l3 3 3-3" fill="none" stroke="#fff" stroke-width="1.2"/></svg></div>
  <div class="abs popout-btn"></div>
  <div class="abs panel-heading" style="left:116px;top:85px">Short-Term Memory</div>
  <div class="abs panel-tag" style="left:116px;top:111px">GRAB</div>
  <div class="abs panel-heading" style="left:116px;top:163px">Working Memory</div>
  <ul class="abs panel-list" style="left:116px;top:186px">
    <li>Cool Down</li><li>Crav</li><li>Go For</li><li>Go-To</li><li>In The Mood For</li><li>Sip</li><li>Soothing</li><li>Stick With</li><li>Throw In/Throw On</li>
  </ul>
  <div class="abs panel-heading" style="left:116px;top:360px">Long-Term Memory</div>
  <ul class="abs panel-list" style="left:116px;top:382px"><li>Give ItA Try</li></ul>
</div>

<nav class="abs main-nav">
  <div class="nav-item" style="top:38px"><div class="home-badge"><svg width="14" height="13" viewBox="0 0 14 13"><path d="M7 0L0 6h2v7h4V9h2v4h4V6h2z" fill="#3a3e43"/></svg></div>QuillaVorn<br>Tutor</div>
  <div class="nav-divider" style="top:127px"></div>
  <div class="nav-item" style="top:149px"><svg width="11" height="15" viewBox="0 0 11 15" style="display:block;margin:0 auto 7px"><path d="M5.5 0A5.5 5.5 0 0 0 0 5.5C0 9.5 5.5 15 5.5 15S11 9.5 11 5.5A5.5 5.5 0 0 0 5.5 0zm0 7.5a2 2 0 1 1 0-4 2 2 0 0 1 0 4z" fill="#fff"/></svg>Daily<br>English</div>
  <div class="nav-divider" style="top:216px"></div>
  <div class="nav-item" style="top:238px"><svg width="15" height="18" viewBox="0 0 15 18" style="display:block;margin:0 auto 8px"><path d="M2 0h11v18H9v-4H6v4H2z" fill="#fff"/><g fill="#3a3e43"><rect x="4" y="2" width="2" height="2"/><rect x="9" y="2" width="2" height="2"/><rect x="4" y="6" width="2" height="2"/><rect x="9" y="6" width="2" height="2"/><rect x="4" y="10" width="2" height="2"/><rect x="9" y="10" width="2" height="2"/></g></svg>Business</div>
</nav>

<div class="abs app-title">QuillaVorn Tutor <svg width="11" height="8" viewBox="0 0 11 8"><path d="M1 1l4.5 4.5L10 1" fill="none" stroke="#2b2f33" stroke-width="2"/></svg></div>
<svg class="abs" style="left:974px;top:44px" width="180" height="26" viewBox="0 0 180 26" fill="none" stroke="#2b2f33" stroke-width="1.6">
  <circle cx="12" cy="13" r="10"/><path d="M7 13l3.5 3.5L17 10"/>
  <circle cx="48" cy="13" r="4"/><path d="M48 2l2 3 3.5-1 1 3.5 3.5 1-1 3.5 3 2-3 2 1 3.5-3.5 1-1 3.5-3.5-1-2 3-2-3-3.5 1-1-3.5-3.5-1 1-3.5-3-2 3-2-1-3.5 3.5-1 1-3.5 3.5 1z"/>
  <path d="M76 19h18l-2.5-3v-6a6.5 6.5 0 0 0-13 0v6zM82 22a3 3 0 0 0 6 0"/><circle cx="91" cy="6" r="3"/>
  <path d="M163 11l4.5 4.5L172 11"/>
</svg>
<div class="abs avatar" role="img" aria-label="User profile photo"></div>
<div class="abs header-rule"></div>

<div class="abs exercise-pill">VOCABULARY REVIEW EXERCISE 3</div>

<div class="abs card sentence-card">
  <div class="abs sentence-line" style="top:20px">Imagine you are running late for</div>
  <div class="abs sentence-line" style="top:37px;right:48px">work and you reach the bus</div>
  <div class="abs sentence-line" style="top:54px;right:33px">stop in the morning. You <b>grab</b> it from</div>
</div>

<div class="abs card chart-card">
  <svg width="824" height="300" viewBox="0 0 824 300" font-family="Poppins, sans-serif">
    <rect x="27" y="22" width="770" height="46" fill="var(--band-long)"/>
    <rect x="27" y="68" width="770" height="102" fill="var(--band-working)"/>
    <rect x="27" y="170" width="770" height="34" fill="var(--band-short)"/>
    <rect x="27" y="204" width="770" height="31" fill="var(--band-forgot)"/>
    <g font-size="9" fill="#666">
      <text x="39" y="47">Long-term Memory</text>
      <text x="39" y="122">Working Memory</text>
      <text x="39" y="190">Short-Term Memory</text>
      <text x="39" y="222">Forgotten Memory</text>
    </g>
    <path d="M306 186C330 186 352 200 391 235" fill="none" stroke="#555" stroke-width="1" stroke-dasharray="1.5 2"/>
    <path d="M395 90C490 90 566 130 569 235" fill="none" stroke="#555" stroke-width="1" stroke-dasharray="1.5 2"/>
    <rect x="303" y="186" width="6" height="49" rx="3" fill="#1f2226"/>
    <rect x="392" y="88" width="7" height="147" rx="3" fill="#1f2226"/>
    <rect x="285" y="162" width="38" height="16" rx="3" fill="#fff"/>
    <text x="304" y="173" font-size="7.5" text-anchor="middle" fill="#333">21 May</text>
    <rect x="374" y="59" width="43" height="17" rx="3" fill="#fff"/>
    <text x="395" y="70" font-size="7.5" text-anchor="middle" fill="#333">22 May</text>
    <line x1="27" y1="235" x2="797" y2="235" stroke="#999"/>
    <g stroke="#999">
      <line x1="41" y1="235" x2="41" y2="242"/><line x1="85" y1="235" x2="85" y2="242"/><line x1="129" y1="235" x2="129" y2="242"/><line x1="173" y1="235" x2="173" y2="242"/><line x1="217" y1="235" x2="217" y2="242"/><line x1="261" y1="235" x2="261" y2="242"/><line x1="305" y1="235" x2="305" y2="242"/><line x1="349" y1="235" x2="349" y2="242"/><line x1="393" y1="235" x2="393" y2="242"/><line x1="437" y1="235" x2="437" y2="242"/><line x1="481" y1="235" x2="481" y2="242"/><line x1="525" y1="235" x2="525" y2="242"/><line x1="569" y1="235" x2="569" y2="242"/><line x1="613" y1="235" x2="613" y2="242"/><line x1="657" y1="235" x2="657" y2="242"/><line x1="701" y1="235" x2="701" y2="242"/><line x1="745" y1="235" x2="745" y2="242"/><line x1="789" y1="235" x2="789" y2="242"/>
    </g>
    <g font-size="7.5" fill="#444" text-anchor="middle">
      <text x="41" y="260">18 May</text><text x="85" y="260">12:00</text><text x="129" y="260">19 May</text><text x="173" y="260">12:00</text><text x="217" y="260">20 May</text><text x="261" y="260">12:00</text><text x="305" y="260">21 May</text><text x="349" y="260">12:00</text><text x="393" y="260">22 May</text><text x="437" y="260">12:00</text><text x="481" y="260">23 May</text><text x="525" y="260">12:00</text><text x="569" y="260">24 May</text><text x="613" y="260">12:00</text><text x="657" y="260">25 May</text><text x="701" y="260">12:00</text><text x="745" y="260">26 May</text><text x="789" y="260">12:00</text>
    </g>
    <text x="412" y="286" font-size="8.5" font-weight="600" text-anchor="middle" fill="#333">DATE RANGE</text>
  </svg>
</div>

<div class="abs section-title">QuillaVorn Tutor Learning Analysis</div>
<div class="abs card analysis-card">
  Lorem ipsum <b>dolor</b> sit amet, consectetur adipiscing elit. Nam <b>rutrum commodo</b> enim id bibendum. Nunc dignissim risus <b>dolor</b>nec finibus dictum eu. Aliquam sit amet euismod metus, quis malesuada erat. Sed at felis quis nulla feugiat cursus at at <b>dolor</b>. Maecenas pretium alquet dapibus. Fusce et eleifend massa.&nbsp; Sed convallis ex mi, at lobortis ligula congue vel.
</div>

<div class="abs scrim"></div>

<!-- expanded vocabulary popup -->
<section class="abs vocab-modal">
  <div class="abs close-btn"><svg width="30" height="30" viewBox="0 0 30 30"><path d="M10 10l10 10M20 10L10 20" stroke="#fff" stroke-width="2"/></svg></div>
  <div class="abs modal-select">ALL <svg style="float:right;margin-top:4px" width="8" height="6" viewBox="0 0 8 6"><path d="M1 1l3 3 3-3" fill="none" stroke="#2b2f33" stroke-width="1.3"/></svg></div>
  <div class="abs modal-rule" style="top:93px"></div>

  <div class="abs group-title" style="top:110px">Short-Term Memory <span class="help">?</span></div>
  <div class="abs group-tag" style="top:141px">GRAB</div>
  <div class="abs modal-rule" style="top:173px"></div>

  <div class="abs group-title" style="top:192px">Working Memory <span class="help">?</span></div>
  <div class="abs chip-row" style="top:224px">
    <span class="chip" style="width:66px">Cool Down</span>
    <span class="chip" style="width:65px">Crav</span>
    <span class="chip" style="width:66px">Go For</span>
    <span class="chip" style="width:65px">Go-To</span>
    <span class="chip" style="width:96px">In The Mood For</span>
    <span class="chip" style="width:58px">Sip</span>
    <span class="chip" style="width:73px">Soothing</span>
    <span class="chip" style="width:73px">Stick With</span>
    <span class="chip" style="width:118px">Throw In/Throw On</span>
  </div>
  <div class="abs modal-rule" style="top:272px"></div>

  <div class="abs group-title" style="top:290px">Long-Term Memory <span class="help">?</span></div>
  <div class="abs chip-row" style="top:323px">
    <span class="chip" style="width:80px">Give ItA Try</span>
  </div>
</section>

</body>
</html>
```